Business Card Design

I want a non fussy clear design. I like Vintage, Retro writing for the main name as it will be a banner for the roof sign.
Company name, address and ph no. I would also like a unisex symbol small in the corner of the card. The colour of the card does not have to be blue. But I do want a bright clean clear card. A head sillohette small in the other corner possibly.

Industry/Entity Type

Business

Contact Information for Business Card

Kestra Hair Design
318 Marlowe Road, Pennick
Ph (09) 4162093

Requirements
Must have
• The back of the card must have appointment time, date dont worry about the location as its obviously on the front of the card

```html
<!DOCTYPE html>
<html lang="en">
<head>
<meta charset="utf-8">
<title>Kestra Hair Design — Business Card</title>
<link href="https://fonts.googleapis.com/css2?family=Federo&family=Poiret+One&display=swap" rel="stylesheet">
<style>
  :root {
    --page: #efe9df;
    --paper-light: #f0dfae;
    --paper-mid: #e2c88c;
    --paper-edge: #cfae6c;
    --ink: #2e1a12;
    --ornament-soft: rgba(150, 118, 80, 0.28);
    --band: rgba(167, 134, 92, 0.45);
    --band-fade: rgba(167, 134, 92, 0.15);
    --corner-mark: #b89866;
    --card-edge: #7a5a33;
  }
  * { box-sizing: border-box; margin: 0; padding: 0; }
  html, body {
    width: 1200px;
    height: 1200px;
    overflow: hidden;
    background: var(--page);
  }
  .sheet {
    position: relative;
    width: 1200px;
    height: 1200px;
  }
  .card {
    position: absolute;
    left: 150px;
    width: 900px;
    height: 510px;
    border: 2px solid var(--card-edge);
    background: radial-gradient(ellipse at 55% 60%, var(--paper-light) 0%, var(--paper-mid) 60%, var(--paper-edge) 100%);
    overflow: hidden;
    font-family: "Poiret One", sans-serif;
    color: var(--ink);
  }
  .card--front { top: 60px; }
  .card--back  { top: 630px; }

  .loop-band {
    position: absolute;
    left: 14px;
    right: 14px;
    height: 30px;
    border-radius: 15px;
    background: linear-gradient(180deg, var(--band-fade), var(--band), var(--band-fade));
  }
  .loop-band--top { top: 12px; }
  .loop-band--bottom { bottom: 12px; }

  .flourish {
    position: absolute;
    left: 0;
    top: 70px;
    width: 900px;
    height: 230px;
    background: radial-gradient(ellipse at 60% 45%, var(--ornament-soft) 0%, rgba(150,118,80,0.12) 45%, rgba(150,118,80,0) 75%);
  }

  .brand-name {
    position: absolute;
    left: 0;
    right: 0;
    top: 128px;
    text-align: center;
    font-family: "Federo", sans-serif;
    font-size: 100px;
    font-weight: 400;
    line-height: 1;
    white-space: nowrap;
    color: var(--ink);
  }

  .contact {
    position: absolute;
    left: 22px;
    top: 372px;
    font-style: normal;
    font-size: 32px;
    line-height: 46px;
    letter-spacing: 1px;
    white-space: nowrap;
  }

  .corner-mark {
    position: absolute;
    right: 36px;
    bottom: 62px;
    width: 72px;
    height: 72px;
    border-radius: 50%;
    background: var(--corner-mark);
  }

  .appointment {
    position: absolute;
    left: 300px;
    top: 190px;
    font-size: 38px;
    line-height: 54px;
    letter-spacing: 1px;
    white-space: nowrap;
  }
</style>
</head>
<body>
<main class="sheet">

  <section class="card card--front" aria-label="Card front">
    <div class="loop-band loop-band--top" role="img" aria-label="Decorative looped border pattern"></div>
    <div class="flourish" role="img" aria-label="Engraved scroll flourish ornament"></div>
    <h1 class="brand-name">Kestra Hair Design</h1>
    <address class="contact">
      <p class="contact__address">318 Marlowe Road, Pennick Ph</p>
      <p class="contact__phone">(09) 4162093</p>
    </address>
    <div class="corner-mark" role="img" aria-label="Space for a small unisex symbol"></div>
    <div class="loop-band loop-band--bottom" role="img" aria-label="Decorative looped border pattern"></div>
  </section>

  <section class="card card--back" aria-label="Card back">
    <div class="loop-band loop-band--top" role="img" aria-label="Decorative looped border pattern"></div>
    <div class="appointment">
      <p class="appointment__time">Appointment time:</p>
      <p class="appointment__date">Date:</p>
    </div>
    <div class="loop-band loop-band--bottom" role="img" aria-label="Decorative looped border pattern"></div>
  </section>

</main>
</body>
</html>
```